Escape Room Flyer Design - Start up. A5

Flyer is for letterbox drops to get interest and let people know that our business exists and to a lesser extent what an escape room is. We have 1 room (the miller's shadows) and a second room coming soon (Varuna's Vault). I have attached our logo and 2 flyers that I have seen in the past that I really like the design of.
Whether you are having a night out with friends or family, celebrating a special event, planning a team-building activity, or simply wanting a diversion from the doldrums of your workweek, The Lock Box will provide you an unforgettable live-action gaming experience.

Target Market(s)

18-25

Industry/Entity Type

Entertainment

Requirements
Must have
• Logo. Phone number 0417 265 839. Website. www.thelockboxhartwell.com
Bookings essential.
Nice to have
• Mystery, a little bit on the darker side than bright colourful and blocky.
"Many Will Enter…Few Will Escape" tag line
60 minute game. Team work. 2-6 players. All ages.
Should not have
• Cartoons, characters, people

```html
<!DOCTYPE html>
<html lang="en">
<head>
<meta charset="utf-8">
<title>The Lock Box – Escape Room Flyer</title>
<link rel="stylesheet" href="https://fonts.googleapis.com/css2?family=Oswald:wght@500;600;700&family=Saira+Semi+Condensed:wght@400&display=swap">
<style>
  :root {
    --bg-deep: #1e151d;
    --bg-glow: #2a2330;
    --gold-light: #f3c46e;
    --gold-mid: #e2a552;
    --gold-dark: #c27c3a;
    --ink-white: #ffffff;
    --ghost-mark: #453a46;
    --panel-top: #5a4e57;
    --panel-bottom: rgba(40, 32, 40, 0);
    --logo-fill: #2a2229;
  }
  * { margin: 0; padding: 0; box-sizing: border-box; }
  html, body {
    width: 849px; height: 1200px; overflow: hidden;
    background: var(--bg-deep);
  }
  .flyer {
    position: relative;
    width: 849px; height: 1200px; overflow: hidden;
    background:
      radial-gradient(circle at 500px 480px, var(--bg-glow) 0%, var(--bg-deep) 60%);
    font-family: "Saira Semi Condensed", "Arial Narrow", sans-serif;
  }
  .gold {
    background: linear-gradient(180deg, var(--gold-light) 0%, var(--gold-mid) 55%, var(--gold-dark) 100%);
    -webkit-background-clip: text; background-clip: text;
    color: transparent;
  }
  .headline-word {
    position: absolute;
    font-family: "Oswald", "Arial Narrow", sans-serif;
    font-weight: 600;
    line-height: 1;
    white-space: nowrap;
    transform-origin: left top;
  }
  .word-many   { left: 54px;  top: 74px;  font-size: 78px; transform: scaleX(0.72); }
  .word-few    { left: 55px;  top: 178px; font-size: 104px; transform: scaleX(0.72); }
  .word-enter  { left: 570px; top: 82px;  font-size: 78px; transform: scaleX(0.72); }
  .word-escape { left: 569px; top: 198px; font-size: 90px; transform: scaleX(0.62); }
  .will-block {
    position: absolute;
    left: 206px; top: 74px; width: 350px; height: 200px;
    background: linear-gradient(135deg, #d99a4d 0%, #f0c47a 40%, #c7803c 70%, #f3cf88 100%);
    display: flex; align-items: center; justify-content: center;
    overflow: hidden;
  }
  .will-block span {
    font-family: "Oswald", "Arial Narrow", sans-serif;
    font-weight: 700;
    font-size: 230px;
    line-height: 1;
    color: #2b1f1d;
    letter-spacing: -6px;
    transform: scaleX(0.9);
    margin-top: -14px;
  }
  .game-facts {
    position: absolute;
    left: 54px; top: 296px;
    font-size: 35px;
    color: var(--ink-white);
    white-space: nowrap;
    transform: scaleX(0.86);
    transform-origin: left top;
  }
  .intro {
    position: absolute;
    left: 56px; top: 421px; width: 736px;
    font-size: 29px;
    line-height: 39px;
    color: var(--gold-light);
    text-align: justify;
    text-align-last: left;
  }
  .intro-inner { display: block; transform: scaleX(0.9); transform-origin: left top; width: 818px; }
  .mystery-mark {
    position: absolute;
    left: 540px; top: 600px;
    font-family: "Oswald", "Arial Narrow", sans-serif;
    font-weight: 700;
    font-size: 400px;
    line-height: 1;
    color: var(--ghost-mark);
  }
  .brand-mark {
    position: absolute;
    left: 57px; top: 719px; width: 315px; height: 414px;
    display: flex; flex-direction: column; align-items: center; justify-content: center; gap: 18px;
  }
  .brand-dot {
    width: 120px; height: 120px; border-radius: 50%;
    background: var(--gold-mid);
  }
  .brand-name {
    font-family: "Oswald", "Arial Narrow", sans-serif;
    font-weight: 600;
    font-size: 52px;
    color: var(--gold-mid);
    text-transform: uppercase;
    letter-spacing: 1px;
  }
  .contact-panel {
    position: absolute;
    left: 497px; top: 960px; width: 293px; height: 170px;
    border-radius: 22px;
    background: linear-gradient(180deg, var(--panel-top) 0%, var(--panel-bottom) 100%);
    text-align: center;
    font-family: "Oswald", "Arial Narrow", sans-serif;
    font-weight: 600;
  }
  .contact-phone {
    display: block; margin-top: 14px;
    font-size: 54px; line-height: 56px;
    word-spacing: 8px;
    transform: scaleX(0.82);
  }
  .contact-web {
    display: block;
    font-size: 25px; line-height: 28px;
    transform: scaleX(0.72);
  }
  .contact-note {
    display: block; margin-top: 6px;
    font-size: 25px; line-height: 30px;
    transform: scaleX(0.78);
  }
</style>
</head>
<body>
  <main class="flyer">
    <h1 class="tagline">
      <span class="headline-word word-many gold">Many</span>
      <span class="will-block"><span>Will</span></span>
      <span class="headline-word word-enter gold">Enter. . .</span>
      <span class="headline-word word-few gold">Few</span>
      <span class="headline-word word-escape gold">ESCAPE»</span>
    </h1>

    <p class="game-facts">60 minute game. Team work. 2-6 players. All ages.</p>

    <p class="intro"><span class="intro-inner">Whether you are having a night out with friends or family, celebrating a special event, planning a team-building activity, or simply wanting a diversion from the doldrums of your workweek, The Lock Box will provide you an unforgettable live-action gaming experience.</span></p>

    <div class="mystery-mark" aria-hidden="true">?</div>

    <div class="brand-mark">
      <span class="brand-dot"></span>
      <span class="brand-name">The Lock Box</span>
    </div>

    <div class="contact-panel">
      <span class="contact-phone gold">0417 265 839</span>
      <span class="contact-web gold">www.thelockboxhartwell.com</span>
      <span class="contact-note gold">Bookings essential.</span>
    </div>
  </main>
</body>
</html>
```